Flyer for Compassion training days

I need a A5-size, single-sided flyer design for my training days. They are weekends in a blend of Compassionate Communication and Buddhist teachings called Palomere Communication. The logo for Palomere that should be included.
The flyer needs room for 1) course title, 2) course dates, location & price, 3) course description, 4) booking info, 5) my picture & short bio, and 6) the palomere.co website (yes, it is 'co' and not 'com).
Updates

Target Market(s)

Women 35-65 years, well-educated, spiritually minded. May have interests like yoga and meditation.

Industry/Entity Type

Health And Wellness

Font styles to use
Sans Serif
Other font styles liked:
• Blue Plaque, Josefina are both great

Colors
fbf289
fdf9cf
cfeae6
33b8a4

Requirements
Must have
• The Palomere logo; my picture.
• Elegance. Calm and expansive feel.
• The poster provided in the project files shows you the kind of information I need to include.
• Colours -- greens and yellows, but the options on pixel harbor are not quite the right shades.
• The logo colour can be changed.
Nice to have
• Classy (but not cliche) image associated with Buddhism; gentle curves similar to those on the business card (see project files).
Should not have
• Dark background. Busy, loud design. Overly 'swirly' design. Images that I have to buy separately.

```html
<!DOCTYPE html>
<html lang="en">
<head>
<meta charset="utf-8">
<title>Palomere Communication Core Course – Flyer</title>
<link href="https://fonts.googleapis.com/css2?family=Open+Sans:wght@400;600;700&family=Montserrat:wght@600;700;800&display=swap" rel="stylesheet">
<style>
  :root{
    --teal:#33b8a4;
    --teal-dark:#1f8f7f;
    --yellow:#fbf289;
    --cream:#fdf9cf;
    --mint:#cfeae6;
    --leaf:#2f6b3a;
    --ink:#3b4a45;
    --white:#ffffff;
  }
  *{box-sizing:border-box;margin:0;padding:0}
  html,body{width:900px;height:1200px;overflow:hidden;background:#f2f2ef}
  body{font-family:"Open Sans",Arial,sans-serif;color:var(--ink)}
  .flyer{position:relative;width:900px;height:1200px;background:var(--white);overflow:hidden}

  .hero-photo{
    position:absolute;left:0;top:100px;width:900px;height:540px;
    background:
      radial-gradient(ellipse 170px 260px at 720px 270px, #9a978a 0%, #7e7b6f 55%, rgba(126,123,111,0) 100%),
      linear-gradient(180deg,#ffffff 0%,#eef5f4 28%,#b9d3c6 46%,#7fa96a 66%,#4c7a3c 100%);
  }

  .brand{position:absolute;left:50px;top:30px;display:flex;align-items:center;gap:14px}
  .brand-dot{width:38px;height:38px;border-radius:50%;background:var(--teal)}
  .brand-name{font-family:"Montserrat",sans-serif;font-weight:700;font-size:32px;color:var(--teal)}

  .course-title{position:absolute;left:50px;top:130px;width:620px;color:var(--leaf)}
  .course-title .values{font-family:"Montserrat",sans-serif;font-weight:600;font-size:24px;line-height:1.3}
  .course-title .name{font-family:"Montserrat",sans-serif;font-weight:800;font-size:34px;line-height:1.2;margin-top:6px}

  .wave{position:absolute;left:0;top:500px;width:900px;height:160px}

  .date-card{
    position:absolute;left:40px;top:440px;width:290px;padding:16px 18px;
    background:var(--cream);border-radius:18px;text-align:center;
    box-shadow:0 4px 14px rgba(0,0,0,.12)
  }
  .date-card .dates{font-family:"Montserrat",sans-serif;font-weight:800;font-size:48px;color:var(--teal);line-height:1}
  .date-card .venue{font-size:17px;font-weight:600;margin-top:8px}
  .date-card .price{font-size:17px;font-weight:600}

  .about-tab{
    position:absolute;right:30px;top:622px;padding:6px 24px;
    background:var(--mint);border-radius:10px 10px 0 0;
    font-family:"Montserrat",sans-serif;font-weight:800;font-size:22px;color:var(--teal-dark)
  }

  .side{position:absolute;left:30px;top:668px;width:290px}
  .booking{background:var(--mint);border-radius:14px;padding:12px 14px;text-align:center}
  .booking .lead{font-family:"Montserrat",sans-serif;font-weight:800;font-size:27px;color:var(--teal-dark)}
  .booking p{font-size:15px;line-height:1.4}
  .booking .email{display:flex;align-items:center;justify-content:center;gap:8px;font-weight:600}
  .facilitator-head{font-family:"Montserrat",sans-serif;font-weight:800;font-size:29px;color:var(--teal);margin-top:14px}
  .bio{font-size:15px;line-height:1.45;margin-top:4px}
  .coaching{margin-top:12px;background:var(--cream);border-left:6px solid var(--teal);border-radius:10px;padding:8px 14px}
  .coaching .who{font-family:"Montserrat",sans-serif;font-weight:800;font-size:20px;color:var(--teal-dark)}
  .coaching p{font-size:15px;font-weight:600}
  .phone{display:flex;align-items:center;gap:10px;margin-top:14px;font-size:18px;font-weight:700;color:var(--leaf)}

  .main{position:absolute;left:345px;top:668px;width:525px}
  .about{font-size:15px;line-height:1.45}
  .explore{margin-top:10px;background:var(--cream);border-radius:14px;padding:10px 22px}
  .explore h2{font-family:"Montserrat",sans-serif;font-weight:700;font-size:18px;color:var(--teal-dark);text-align:center}
  .explore ul{list-style:none;margin-top:4px}
  .explore li{font-size:14.5px;line-height:1.35;text-align:center;padding:4px 0;border-bottom:2px solid var(--teal)}
  .audience{margin-top:10px;background:var(--teal);color:var(--white);border-radius:12px;padding:10px 16px;font-size:14.5px;line-height:1.4}
  .website{margin-top:10px;text-align:right;font-family:"Montserrat",sans-serif;font-weight:800;font-size:26px;color:var(--teal-dark)}
</style>
</head>
<body>
<main class="flyer">
  <div class="hero-photo" role="img" aria-label="Photograph of a serene stone Buddha head beside a green valley of trees under a pale sky"></div>

  <div class="brand">
    <span class="brand-dot"></span>
    <span class="brand-name">Palomere</span>
  </div>

  <header class="course-title">
    <p class="values">Mindfulness • Kindness •<br>Compassionate Communication =</p>
    <h1 class="name">Palomere Communication<br>Core Course</h1>
  </header>

  <svg class="wave" viewBox="0 0 900 160" preserveAspectRatio="none" aria-hidden="true">
    <path d="M0 90 C250 35 560 50 900 15 L900 160 L0 160 Z" fill="var(--yellow)"/>
    <path d="M0 125 C260 70 580 85 900 50 L900 160 L0 160 Z" fill="var(--white)"/>
  </svg>

  <section class="date-card">
    <p class="dates">11-12 Dec</p>
    <p class="venue">Fernhill Centre, Dunmore</p>
    <p class="price">(£125/100)</p>
  </section>

  <div class="about-tab">ABOUT US:</div>

  <aside class="side">
    <div class="booking">
      <p class="lead">Book online</p>
      <p>at TicketLoom</p>
      <p>or</p>
      <p class="email">
        <svg width="20" height="14" viewBox="0 0 20 14" aria-hidden="true"><rect x="1" y="1" width="18" height="12" rx="2" fill="none" stroke="var(--teal-dark)" stroke-width="2"/><path d="M1 2 L10 8 L19 2" fill="none" stroke="var(--teal-dark)" stroke-width="2"/></svg>
        marisol@palomere.co
      </p>
    </div>
    <h2 class="facilitator-head">Facilitator:</h2>
    <p class="bio">Marisol Trevane is an experienced group facilitator, having worked with a range of organisations and presented at a number of festivals &amp; conferences.</p>
    <div class="coaching">
      <p class="who">Marisol offers</p>
      <p>coaching in Palomere Communication.</p>
    </div>
    <p class="phone">
      <svg width="22" height="22" viewBox="0 0 24 24" aria-hidden="true"><path d="M6.6 10.8a15 15 0 0 0 6.6 6.6l2.2-2.2a1 1 0 0 1 1-.25 11.4 11.4 0 0 0 3.6.57 1 1 0 0 1 1 1V20a1 1 0 0 1-1 1A17 17 0 0 1 3 4a1 1 0 0 1 1-1h3.5a1 1 0 0 1 1 1c0 1.25.2 2.45.57 3.57a1 1 0 0 1-.25 1z" fill="var(--teal)"/></svg>
      +44 1632 960 555
    </p>
  </aside>

  <section class="main">
    <p class="about">Palomere Communication can help you increase awareness &amp; compassion in everyday speech (with yourself &amp; others), better understand your own patterns, and build resilience to challenging situations. Choose from:</p>
    <div class="explore">
      <h2>In this 2-day Core Course, we’ll explore:</h2>
      <ul>
        <li>Compassionate Communication</li>
        <li>Buddhist teachings on Right Speech, loving kindness, Right Effort, and more</li>
        <li>mindfulness practices</li>
        <li>choices available to us in our everyday speech</li>
      </ul>
    </div>
    <p class="audience">This workshop will be of interest if you’d like to improve personal and/or professional relationships. Open to all, best suited to those with at least 1 year’s experience with Mindfulness, Buddhism, or Compassionate Communication / NVC.</p>
    <p class="website">www.palomere.co</p>
  </section>
</main>
</body>
</html>
```